lunch and dinne(al a carte) menus

we are a medium sized licenced club that has taken back the dining in the club
in the western suburbs of sydney working class with a rugby league base
our logo is a wolf kelford hawks

Reason: We have changed the name to Bluegate grill it could be done as Bluegate or Bluegate or Bluegate We need a lunch menu and a seperate dinner menu eg Bluegate grill l u n c h or Bluegate grill d i n n e r

Reason: Weve changed the name

Target Market(s)

young families, working class rugby leagues sporty types

Industry/Entity Type

Club

Requirements
Must have
• user friendly

```html
<!DOCTYPE html>
<html lang="en">
<head>
<meta charset="utf-8">
<title>Bluegate Grill – Lunch Menu</title>
<link href="https://fonts.googleapis.com/css2?family=Alfa+Slab+One&family=Roboto+Condensed:ital,wght@0,700;1,700&display=swap" rel="stylesheet">
<style>
  :root {
    --page: #ffffff;
    --field: #07921f;
    --field-line: #40ad50;
    --ink: #111111;
    --club-gold: #f5b324;
  }
  html, body {
    margin: 0;
    padding: 0;
    width: 1000px;
    height: 1200px;
    overflow: hidden;
    background: var(--page);
  }
  .menu-board {
    position: relative;
    width: 1000px;
    height: 1200px;
    background: var(--page);
  }
  .field {
    position: absolute;
    left: 115px;
    top: 0;
    width: 772px;
    height: 1200px;
    background: var(--field);
  }
  .field-lines {
    position: absolute;
    left: 0;
    top: 0;
  }
  .club-name {
    position: absolute;
    left: 182px;
    top: 76px;
    display: flex;
    align-items: center;
    gap: 9px;
    font-family: "Roboto Condensed", sans-serif;
    font-weight: 700;
    font-style: normal;
    font-size: 28px;
    line-height: 1;
    color: var(--club-gold);
    text-transform: uppercase;
    white-space: nowrap;
  }
  .club-name .club-dot {
    width: 20px;
    height: 20px;
    border-radius: 50%;
    background: var(--club-gold);
  }
  .menu-title {
    position: absolute;
    left: 424px;
    top: 54px;
    width: 338px;
    margin: 0;
    font-family: "Alfa Slab One", serif;
    font-weight: 400;
    font-size: 36px;
    line-height: 45px;
    color: var(--ink);
    text-align: center;
    white-space: nowrap;
  }
  .menu-title .meal {
    letter-spacing: 2px;
  }
  .price-head, .dish, .dish-note, .price {
    position: absolute;
    font-family: "Roboto Condensed", sans-serif;
    font-weight: 700;
    font-style: italic;
    color: var(--ink);
    white-space: nowrap;
    line-height: 1;
  }
  .price-head { font-size: 16px; top: 229px; }
  .price-head.member { left: 736px; }
  .price-head.visitor { left: 812px; }
  .dish { left: 179px; font-size: 19px; transform: scaleX(0.86); transform-origin: left; }
  .dish-note { left: 179px; font-size: 17px; transform: scaleX(0.86); transform-origin: left; }
  .price { font-size: 19px; text-align: right; width: 60px; }
  .price.member { left: 702px; }
  .price.visitor { left: 770px; }
  .section-rule {
    position: absolute;
    left: 179px;
    top: 538px;
    width: 578px;
    height: 2px;
    background: repeating-linear-gradient(90deg, var(--ink) 0 5px, transparent 5px 7px);
  }
</style>
</head>
<body>
<main class="menu-board">
  <div class="field">
    <svg class="field-lines" width="772" height="1200" viewBox="0 0 772 1200" aria-hidden="true">
      <g fill="var(--field-line)">
        <rect x="0" y="36" width="772" height="16"/>
        <rect x="0" y="128" width="772" height="18"/>
        <rect x="0" y="218" width="772" height="18"/>
        <rect x="0" y="310" width="772" height="18"/>
        <rect x="0" y="405" width="772" height="18"/>
        <rect x="0" y="497" width="772" height="18"/>
        <rect x="0" y="590" width="772" height="18"/>
        <rect x="0" y="685" width="772" height="18"/>
        <rect x="0" y="777" width="772" height="18"/>
        <rect x="0" y="867" width="772" height="18"/>
        <rect x="0" y="962" width="772" height="18"/>
        <rect x="0" y="1053" width="772" height="18"/>
        <rect x="0" y="1146" width="772" height="18"/>
        <rect x="32" y="36" width="22" height="1128"/>
        <rect x="713" y="36" width="23" height="1128"/>
      </g>
    </svg>
  </div>

  <div class="club-name"><span class="club-dot"></span>Kelford Hawks</div>

  <h1 class="menu-title">Bluegate Grill<br><span class="meal">Lunch Menu</span></h1>

  <span class="price-head member">Member</span>
  <span class="price-head visitor">Visitor</span>

  <span class="dish" style="top:309px">Vegetarian Spring Rolls (4) with Rice</span>
  <span class="price member" style="top:309px">$8</span>
  <span class="price visitor" style="top:309px">$10</span>

  <span class="dish" style="top:381px">Club Sandwich with Chips</span>
  <span class="price member" style="top:381px">$8</span>
  <span class="price visitor" style="top:381px">$10</span>
  <span class="dish-note" style="top:419px">(chicken, bacon, cheese, tomato, lettuce &amp; mayo)</span>

  <span class="dish" style="top:490px">Home Made Quiche with Chips</span>
  <span class="price member" style="top:490px">$8</span>
  <span class="price visitor" style="top:490px">$10</span>

  <div class="section-rule"></div>

  <span class="dish" style="top:564px">T-bone with Chips and Salad</span>
  <span class="price member" style="top:564px">$10</span>
  <span class="price visitor" style="top:564px">$12</span>

  <span class="dish" style="top:636px">Open Hamburger with the Works and Chips</span>
  <span class="price member" style="top:636px">$10</span>
  <span class="price visitor" style="top:636px">$12</span>

  <span class="dish" style="top:709px">Cajun Chicken Burger with Chips</span>
  <span class="price member" style="top:709px">$10</span>
  <span class="price visitor" style="top:709px">$12</span>

  <span class="dish" style="top:782px">Spaghetti Bolognese</span>
  <span class="price member" style="top:782px">$10</span>
  <span class="price visitor" style="top:782px">$12</span>

  <span class="dish" style="top:854px">Chicken Caesar Salad</span>
  <span class="price member" style="top:854px">$10</span>
  <span class="price visitor" style="top:854px">$12</span>

  <span class="dish" style="top:927px">Bangers &amp; Mash (1 Thick and 1 Thin Sausage)</span>
  <span class="price member" style="top:927px">$10</span>
  <span class="price visitor" style="top:927px">$12</span>

  <span class="dish" style="top:1000px">Vegetarian Lasagne with Chips and Salad</span>
  <span class="price member" style="top:1000px">$10</span>
  <span class="price visitor" style="top:1000px">$12</span>
</main>
</body>
</html>
```